Keystone Wiring LLC

I need a business card containing the following:

KeystoneWiringLLC
Certified Master Electrician
Licensed and insured
"powered by excellence"

Dale Brunholt. Owen Taliferro
484-215-6390 215-846-3027

KeystoneWiringLLC.com

red white and blue color scheme

Brief has been updated. colour scheme is included, tagline is changed thanks Added Wednesday, August 30, 2017

Industry/Entity Type

Electric Company

Contact Information for Business Card

Red white and blue coloring

Colors
ec1f27
0456a4
ffffff

Requirements
Must have
• Keystone Wiring
• Certified master Electrician
• Liscensed and insured
• "Powered by excellence"
• Dale Brunholt. 4842156390
• Owen Taliferro. 2158463027

```html
<!DOCTYPE html>
<html lang="en">
<head>
<meta charset="utf-8">
<title>Keystone Wiring LLC – Business Card</title>
<link rel="stylesheet" href="https://fonts.googleapis.com/css2?family=Didact+Gothic&display=swap">
<style>
  :root {
    --stage: #6f7d90;
    --card-navy: #021f3f;
    --card-blue: #0456a4;
    --band-red: #ec1f27;
    --band-red-dark: #c8161d;
    --text-white: #ffffff;
    --accent-red: #f2434a;
  }
  * { margin: 0; padding: 0; box-sizing: border-box; }
  html, body { width: 1200px; height: 810px; overflow: hidden; }
  body {
    background: var(--stage);
    font-family: "Didact Gothic", "Helvetica Neue", Arial, sans-serif;
    position: relative;
  }
  .card {
    position: absolute;
    top: 250px;
    width: 540px;
    height: 310px;
    background: linear-gradient(135deg, var(--card-navy) 0%, var(--card-navy) 45%, var(--card-blue) 100%);
    box-shadow: 0 14px 30px rgba(0,0,0,0.35);
    overflow: hidden;
  }
  .card--contact { left: 40px; }
  .card--brand { left: 620px; }
  .card__band {
    position: absolute;
    left: 0; right: 0; bottom: 0;
    height: 26px;
    background: linear-gradient(to bottom, var(--band-red), var(--band-red-dark));
  }
  .wordmark {
    color: var(--text-white);
    line-height: 1;
    white-space: nowrap;
  }
  .card--contact .wordmark {
    position: absolute; left: 40px; top: 40px; font-size: 30px;
  }
  .owners {
    position: absolute; left: 40px; top: 100px;
    color: var(--accent-red);
    font-size: 19px;
    line-height: 1.35;
  }
  .contact-list {
    position: absolute; left: 290px; top: 150px;
    list-style: none;
    color: var(--text-white);
    font-size: 15px;
    line-height: 1.35;
  }
  .contact-list li {
    display: flex; align-items: flex-start; gap: 9px;
    margin-bottom: 10px;
  }
  .contact-list svg { width: 13px; height: 13px; margin-top: 3px; flex: none; }
  .card--brand .wordmark {
    position: absolute; left: 150px; top: 72px; font-size: 38px;
  }
  .tagline {
    position: absolute; left: 150px; top: 140px;
    color: var(--accent-red);
    font-size: 13px;
    letter-spacing: 1.6px;
    line-height: 1.45;
    list-style: none;
  }
</style>
</head>
<body>
  <section class="card card--contact" aria-label="Business card, contact side">
    <div class="wordmark">Keystone Wiring LLC</div>
    <div class="owners">
      <p>Dale Brunholt</p>
      <p>Owen Taliferro</p>
    </div>
    <ul class="contact-list">
      <li>
        <svg viewBox="0 0 12 12" aria-hidden="true"><path d="M6 0.5a4 4 0 0 0-4 4c0 3 4 7 4 7s4-4 4-7a4 4 0 0 0-4-4z" fill="#ffffff"/><circle cx="6" cy="4.5" r="1.5" fill="#021f3f"/></svg>
        <span>1250 Millbrook Road<br>Riverton, WY 82501</span>
      </li>
      <li>
        <svg viewBox="0 0 12 12" aria-hidden="true"><path d="M2.5 1l2 2.2-1 1.3c.8 1.6 2 2.8 3.6 3.6l1.3-1 2.2 2-1.2 1.6C5.2 10.5 1.5 6.8.9 2.2z" fill="#ffffff"/></svg>
        <span>484-215-6390<br>215-846-3027</span>
      </li>
      <li>
        <svg viewBox="0 0 12 12" aria-hidden="true"><g fill="none" stroke="#ffffff" stroke-width="1.2"><circle cx="6" cy="6" r="5"/><ellipse cx="6" cy="6" rx="2.2" ry="5"/><path d="M1 6h10"/></g></svg>
        <span>KeystoneWiringLLC.com</span>
      </li>
    </ul>
    <div class="card__band"></div>
  </section>

  <section class="card card--brand" aria-label="Business card, brand side">
    <div class="wordmark">Keystone Wiring LLC</div>
    <ul class="tagline">
      <li>KeystoneWiringLLC</li>
      <li>Certified Master Electrician</li>
      <li>Licensed and insured</li>
      <li>"powered by excellence"</li>
    </ul>
    <div class="card__band"></div>
  </section>
</body>
</html>
```